Doctors Office Web Design

Name of the business is Lian-Hua Qiu M.D.
We need a web design that is attractive for women that want to see Dr. Lian-Hua Qiu for Obstetrician Gynecology and Pregnancy care. Dr. Qiu earned her degree from Harbor Crest Medical College of obstetrician gynecology. We want to attract women of child bearing ages to come to our offices for health, education, and pregnancies.

Please visit http://www.drqiucare-example.com/ to help you get a feel for who we are. We will be adding some pictures and logo in the next few days.

We are looking for to have pages for and tabs including
About Us- History, Our Staff, Dr. Qiu
Patient Information- Appointments, E-Prescriptions, Payments Accepted, Insurance
Health- General, Sexual, Mental, Affiliates
Pregnancy- Minimally invasive surgery(our specialty), 4-D Ultra Sound, Hospital Affiliations
Media- News,Pictures, Videos
Locations- Palmvale Office, Marlow Office

The colors we would like to use are pastel colors, magenta, and plum

Target Market(s)

Women of all ages with an emphasis on 25-65 year olds

Industry/Entity Type

Business

Requirements
Must have
• Needs to include a location for a our videos and pictures that I will submit shortly. We also want a map to our location or atleast a place for one.
Nice to have
• A place for a google map of our office locations.

```html
<!DOCTYPE html>
<html lang="en">
<head>
<meta charset="utf-8">
<title>Lian-Hua Qiu M.D. — Prenatal Care</title>
<link rel="stylesheet" href="https://fonts.googleapis.com/css2?family=Questrial&family=Mulish:wght@600;700&family=Cormorant+Garamond:ital,wght@1,500&display=swap">
<style>
  :root {
    --page-top: #c9dbf1;
    --page-bottom: #8fb2e0;
    --band-top: #7da2d6;
    --panel: #2f5ea6;
    --frame: #1d3153;
    --column: #1d3d73;
    --card: #7fa6dc;
    --content-box: #a8bfe0;
    --heading: #a9c4ec;
    --tab: #6f9dd8;
    --logo-box: #7ba3d8;
    --ink: #111;
    --ink-dark-blue: #1b3a78;
    --white: #fff;
    --search: #1a2c52;
  }
  * { box-sizing: border-box; margin: 0; padding: 0; }
  html, body { width: 1200px; height: 888px; overflow: hidden; }
  body {
    position: relative;
    font-family: "Questrial", sans-serif;
    color: var(--ink);
    background: linear-gradient(180deg, var(--page-top) 0%, #b5cdea 45%, var(--page-bottom) 100%);
  }
  .top-band { position: absolute; left: 0; top: 0; width: 1200px; height: 4px; background: var(--band-top); }
  .backdrop-art {
    position: absolute; left: 0; top: 4px; width: 1200px; height: 858px;
    background: radial-gradient(ellipse at 12% 55%, rgba(255,255,255,.35), transparent 40%),
                radial-gradient(ellipse at 92% 30%, rgba(255,255,255,.3), transparent 35%);
  }
  .logo {
    position: absolute; left: 195px; top: 11px; width: 190px; height: 58px;
    background: var(--logo-box);
    display: flex; align-items: center; justify-content: center;
    font-family: "Mulish", sans-serif; font-weight: 700; font-size: 21px; letter-spacing: .5px;
  }
  .main-nav { position: absolute; left: 0; top: 0; }
  .main-nav a {
    position: absolute; top: 47px; font-size: 17px; color: var(--ink); text-decoration: none; white-space: nowrap;
  }
  .main-nav a.active {
    top: 43px; height: 35px; padding: 4px 6px 0; background: var(--tab); border-radius: 6px 6px 0 0;
  }
  .panel { position: absolute; left: 179px; top: 92px; width: 835px; height: 770px; background: var(--panel); }
  .banner-frame {
    position: absolute; left: 184px; top: 74px; width: 821px; height: 154px;
    background: var(--frame); border-radius: 12px;
  }
  .banner-photo {
    position: absolute; left: 196px; top: 80px; width: 798px; height: 133px; border-radius: 6px;
    background: linear-gradient(90deg, #f1ede8 0%, #e0c7b3 25%, #b3785a 50%, #8a5038 70%, #7a4330 100%);
  }
  .banner-text { position: absolute; right: 244px; top: 94px; text-align: right; color: var(--white); }
  .banner-text .tagline {
    font-family: "Cormorant Garamond", serif; font-style: italic; font-weight: 500;
    font-size: 29px; line-height: 28px; display: block;
  }
  .banner-text .name { font-size: 21px; display: block; margin-top: 4px; }
  .banner-text .title { font-family: "Mulish", sans-serif; font-weight: 700; font-size: 20px; display: block; }
  .page-title {
    position: absolute; left: 197px; top: 234px; width: 512px; padding-bottom: 2px;
    font-family: "Mulish", sans-serif; font-weight: 700; font-size: 20.5px; color: var(--heading);
    border-bottom: 1px solid var(--heading);
  }
  .search {
    position: absolute; left: 829px; top: 239px; width: 145px; height: 16px; border-radius: 8px;
    background: var(--search); color: var(--white); font-size: 12px; padding-left: 8px; line-height: 16px;
  }
  .search-icon { position: absolute; left: 975px; top: 239px; }
  .article {
    position: absolute; left: 194px; top: 269px; width: 534px; height: 378px;
    background: var(--content-box); border-radius: 6px; padding: 11px 10px 0 9px;
    font-size: 10.6px; line-height: 16px;
  }
  .article p { margin-bottom: 16px; }
  .article ul { list-style: none; padding-left: 50px; }
  .related-title {
    position: absolute; left: 197px; top: 654px;
    font-family: "Mulish", sans-serif; font-weight: 700; font-size: 20px; color: var(--heading);
  }
  .related-card { position: absolute; top: 687px; width: 170px; text-align: center; }
  .related-card .thumb { height: 149px; border-radius: 8px; }
  .related-card .caption {
    display: block; margin-top: 5px; color: var(--white);
    font-family: "Mulish", sans-serif; font-weight: 700; font-size: 11.5px;
  }
  .sidebar {
    position: absolute; left: 744px; top: 268px; width: 262px; height: 590px;
    background: var(--column); border-radius: 10px;
  }
  .health-menu {
    position: absolute; left: 750px; top: 277px; width: 250px; height: 112px;
    background: var(--card); border-radius: 5px; padding: 12px 8px 0 8px;
  }
  .health-menu h2 { font-weight: 400; font-size: 21px; line-height: 24px; border-bottom: 1px solid #2d4c84; padding-bottom: 2px; }
  .health-menu a { display: block; font-size: 14.5px; line-height: 16px; color: #1b2f5a; text-decoration: none; padding-left: 2px; }
  .health-menu h2 + a { margin-top: 5px; }
  .side-feature { position: absolute; left: 750px; width: 249px; border-radius: 5px; overflow: hidden; }
  .side-feature .media { height: 154px; }
  .side-feature .band { background: var(--card); padding: 1px 6px 0; height: 35px; font-size: 14px; line-height: 16px; }
  .side-feature .band a { color: var(--ink-dark-blue); text-decoration: none; }
  .map-feature .media { height: 193px; }
  .map-feature .band { color: var(--white); font-size: 14.5px; line-height: 35px; padding-left: 15px; }
  .map-feature .band a { color: var(--ink-dark-blue); }
  .footer {
    position: absolute; left: 0; top: 862px; width: 1200px; height: 26px; background: var(--white);
    text-align: center; font-size: 11px; line-height: 28px; color: var(--ink);
  }
  .footer a { color: var(--ink); text-decoration: none; }
</style>
</head>
<body>
  <div class="top-band"></div>
  <div class="backdrop-art" role="img" aria-label="Soft pale blue leaf pattern with a smiling baby fading into the background"></div>

  <div class="logo">LOGO</div>
  <nav class="main-nav">
    <a href="#" style="left:401px">home</a>
    <a href="#" style="left:472px">about</a>
    <a href="#" style="left:541px">patients info</a>
    <a href="#" class="active" style="left:654px">health</a>
    <a href="#" style="left:733px">pregnancy</a>
    <a href="#" style="left:841px">media</a>
    <a href="#" style="left:920px">locations</a>
  </nav>

  <div class="panel"></div>
  <div class="banner-frame"></div>
  <div class="banner-photo" role="img" aria-label="Doctor listening with a stethoscope to a pregnant belly"></div>
  <div class="banner-text">
    <span class="tagline">Serving all areas</span>
    <span class="tagline">of women’s health,</span>
    <span class="name">lian-hua qiu, m.d., facog</span>
    <span class="title">Obstetrician/Gynecologist</span>
  </div>

  <h1 class="page-title">Prenatal care keeps you and your baby healthy</h1>
  <div class="search">search...</div>
  <svg class="search-icon" width="14" height="14" viewBox="0 0 14 14" aria-hidden="true">
    <circle cx="5.5" cy="5.5" r="3.8" fill="none" stroke="#9fbbe6" stroke-width="2"/>
    <line x1="8.3" y1="8.3" x2="12.5" y2="12.5" stroke="#9fbbe6" stroke-width="2.4" stroke-linecap="round"/>
  </svg>

  <article class="article">
    <p>You’re having a baby! It’s important to take very good care of yourself so that both you and baby are healthy. Taking good care of yourself includes getting prenatal care. You can see an obstetrician/gynecologist (OB/GYN) for prenatal care, or a family practice doctor, a certified-nurse midwife or other health professional.</p>
    <p>Regular prenatal care helps you and your health provider monitor how your pregnancy is going. It also helps spot any potential health problems before they become serious. Some pregnant women may experience complications like gestational diabetes or preeclampsia. But with regular prenatal care, you’ll be better able to manage any health issues that may come up.</p>
    <p>During your prenatal care visits, your provider will calculate your due date and check if there are any vaccinations you need. You’ll also get to experience the exciting moment of seeing your baby for the first time with an ultrasound. An ultrasound uses sound waves to show a picture of the baby on a screen. Many providers offer an ultrasound examination to all pregnant women.</p>
    <p style="margin-bottom:4px">Your provider will perform prenatal tests to ensure baby is growing healthy. Some of these tests include:</p>
    <ul>
      <li>amniocentesis (test for certain birth defects)</li>
      <li>chorionic virus sampling or CVS (test for certain birth defects)</li>
      <li>glucose screening (monitor blood sugar)</li>
      <li>cystic fibrosis carrier screening (check for cystic fibrosis gene)</li>
      <li>maternal blood screening (check for neural tube defects)</li>
    </ul>
  </article>

  <h2 class="related-title">Related Articles</h2>
  <div class="related-card" style="left:198px">
    <div class="thumb" role="img" aria-label="Pregnant woman at a check-up with her doctor" style="background:linear-gradient(160deg,#f3f3f6,#d9d4dc 60%,#b7b6c9)"></div>
    <span class="caption">Time for Delivery</span>
  </div>
  <div class="related-card" style="left:376px">
    <div class="thumb" role="img" aria-label="Two smiling young women" style="background:linear-gradient(160deg,#f4efe9,#d9b39a 55%,#a9876c)"></div>
    <span class="caption">Pregnancy Testing</span>
  </div>
  <div class="related-card" style="left:554px">
    <div class="thumb" role="img" aria-label="Laughing baby with hands at its mouth" style="background:linear-gradient(160deg,#fbfbfb,#f1ddd2 60%,#e6c2ae)"></div>
    <span class="caption">Post Pregnancy Concerns</span>
  </div>

  <aside class="sidebar"></aside>
  <div class="health-menu">
    <h2>Health</h2>
    <a href="#">General »</a>
    <a href="#">Sexual »</a>
    <a href="#">Mental »</a>
    <a href="#">Affiliates »</a>
  </div>

  <div class="side-feature" style="top:407px">
    <div class="media" role="img" aria-label="Newborn hand holding a parent's finger" style="background:linear-gradient(150deg,#c9c6cf,#d7b2a0 50%,#8e6c5e)"></div>
    <div class="band">Worried about breastfeeding?<br><a href="#">Post Pregnancy Concerns »</a></div>
  </div>

  <div class="side-feature map-feature" style="top:614px">
    <div class="media" role="img" aria-label="Street map showing the office location" style="background:linear-gradient(180deg,#ecebe5,#e3e1d9)"></div>
    <div class="band">Find Us at these Two <a href="#">Locations</a> »</div>
  </div>

  <footer class="footer">
    <a href="#">home</a> | <a href="#">about</a> | <a href="#">contact</a> | <a href="#">site map</a> | <a href="#">disclaimer</a>
  </footer>
</body>
</html>
```